Salon industry management software needs folded self-mailer flyer for direct mail

We are looking for a postcard / flyer folded self-mailer design for an 8.5" x 11" card stock printed both sides and folded in half to be the same end size as a 5.5" x 8.5" postcard. So, DOUBLE THE CONTENT from a regular postcard. See mailer attachment for the format we are looking for.
This will be to advertise our salon and spa management software to hair salons, spas, tanning salons, tattoo studios, and massage therapists. Our websites are https://parlorpilot-systems.net/ and https://brightloomsuite.net/ where you can get inspiration and some content. We have two software applications. Lumera is a desktop application and Vantel is a web application, so you can focus on one, both or a combination.
We need space for a QR code and of course mailing information.

Target Market(s)

salon, spa, tanning, tattoo, massage

Requirements
Must have
• content for four 5.5" x 8.5" pages including mailing info
Nice to have
• call to action, qr code

```html
<!DOCTYPE html>
<html lang="en">
<head>
<meta charset="utf-8">
<title>Lumera Salon &amp; Spa Software Mailer</title>
<link rel="stylesheet" href="https://fonts.googleapis.com/css2?family=Roboto:wght@400;500;700&display=swap">
<style>
:root{
  --bg:#e9eaec;
  --paper:#ffffff;
  --green:#1f9a5a;
  --green-dark:#17734a;
  --teal:#3e6a72;
  --slate:#4a5a66;
  --blue-head:#1d87b7;
  --blue-label:#1fa3dd;
  --grey-text:#5e6368;
  --line:#333;
}
*{box-sizing:border-box;margin:0;padding:0}
html,body{width:1050px;height:1200px;overflow:hidden;background:var(--bg);font-family:"Roboto",Arial,sans-serif}
.page{position:absolute;top:280px;width:495px;height:640px;background:var(--paper);overflow:hidden;box-shadow:0 2px 8px rgba(0,0,0,.18)}
.page--front{left:20px}
.page--inside{left:535px}

/* front */
.photo-top{position:absolute;left:0;top:0;width:495px;height:321px;background:linear-gradient(90deg,#f7f7f6 0%,#ecebe7 35%,#c4c0b2 65%,#6c6a62 100%)}
.address-lines{position:absolute;left:32px;top:103px;width:180px}
.address-lines span{display:block;height:1px;background:var(--line);margin-bottom:30px}
.stamp-box{position:absolute;left:32px;top:235px;width:53px;height:62px;border:1px solid #222;background:#fff;display:flex;align-items:center;justify-content:center;font-size:11px;font-style:italic;transform:rotate(180deg);color:#222}
.hero-band{position:absolute;left:0;top:321px;width:495px;height:234px;background:linear-gradient(90deg,var(--green) 0%,var(--green-dark) 55%,var(--teal) 100%)}
.hero-photo{position:absolute;left:290px;top:321px;width:205px;height:234px;background:linear-gradient(90deg,rgba(31,154,90,0) 0%,#2d5a4c 40%,#3b4c45 100%)}
.hero-shade{position:absolute;left:0;top:365px;width:272px;height:108px;background:rgba(20,60,45,.35)}
.hero-title{position:absolute;left:23px;top:366px;color:#fff}
.hero-title h1{font-size:28px;font-weight:700;line-height:32px}
.hero-title h2{font-size:23px;font-weight:700;line-height:28px}
.hero-title p{font-size:14px;line-height:17px;margin-top:9px;font-weight:400}
.footer-strip{position:absolute;left:0;top:555px;width:495px;height:85px;background:linear-gradient(180deg,#fff 0%,#f2f3f3 100%)}
.devices{position:absolute;left:20px;top:505px;width:232px;height:95px;background:linear-gradient(135deg,#2b2f33 0%,#4f5a63 50%,#c7ccd1 100%);border-radius:4px}
.brand{position:absolute;top:583px;font-size:22px;font-weight:500;color:var(--teal);line-height:26px}
.brand--lumera{left:267px}
.brand--vantel{left:361px;display:flex;align-items:center;gap:7px}
.brand--vantel i{display:inline-block;width:13px;height:13px;border-radius:50%;background:var(--blue-head)}

/* inside */
.features{position:absolute;left:0;top:0;width:495px;height:321px;background:linear-gradient(90deg,#fafafa 0%,#ffffff 60%,#eef0f1 100%)}
.label{position:absolute;height:24px;color:#fff;font-size:16px;font-weight:500;display:flex;align-items:center;justify-content:center}
.label--features{left:93px;top:29px;width:311px;background:linear-gradient(90deg,var(--green) 0%,var(--slate) 100%)}
.label--why{left:93px;top:339px;width:311px;background:linear-gradient(90deg,var(--blue-label) 0%,var(--green) 100%)}
.feature{position:absolute;width:210px}
.feature h3{font-size:11px;font-weight:500;color:var(--blue-head);letter-spacing:.1px;line-height:13px}
.feature p{font-size:9.5px;color:var(--grey-text);line-height:13px;margin-top:1px}
.barber-photo{position:absolute;left:321px;top:214px;width:174px;height:116px;background:linear-gradient(135deg,#7a5a3e 0%,#3a3530 50%,#c9c2b5 100%)}
.why-band{position:absolute;left:0;top:321px;width:495px;height:319px;background:linear-gradient(90deg,var(--green) 0%,var(--green-dark) 50%,var(--teal) 100%)}
.why-bottom{position:absolute;left:0;top:541px;width:495px;height:99px;background:linear-gradient(90deg,rgba(60,140,100,.6) 0%,rgba(60,80,80,.6) 100%)}
.why-intro{position:absolute;left:22px;top:371px;width:451px;color:#fff;font-size:8.8px;line-height:13px;text-align:center}
.why-point{position:absolute;left:20px;width:318px;color:#fff}
.why-point h3{font-size:11px;font-weight:500;line-height:13px}
.why-point p{font-size:8.8px;line-height:13px;margin-top:2px}
.circle-photo{position:absolute;left:345px;top:424px;width:136px;height:136px;border-radius:50%;background:linear-gradient(135deg,#dcd2c4 0%,#8c8a86 60%,#3c3e44 100%);box-shadow:0 0 0 4px rgba(255,255,255,.15)}
</style>
</head>
<body>

<section class="page page--front">
  <div class="photo-top" role="img" aria-label="Faded photo of a man with earphones using a laptop, printed upside down"></div>
  <div class="address-lines"><span></span><span></span><span></span><span></span></div>
  <div class="stamp-box">Stamp</div>
  <div class="hero-band"></div>
  <div class="hero-photo" role="img" aria-label="Smiling salon stylist with long hair in a salon"></div>
  <div class="hero-shade"></div>
  <div class="hero-title">
    <h1>Salon &amp; Spa</h1>
    <h2>Management Software</h2>
    <p>Get the tools you need to grow<br>your business!</p>
  </div>
  <div class="footer-strip"></div>
  <div class="devices" role="img" aria-label="Software screens shown on laptop, desktop, tablet and phone"></div>
  <div class="brand brand--lumera">Lumera</div>
  <div class="brand brand--vantel"><i></i>Vantel</div>
</section>

<section class="page page--inside">
  <div class="features"></div>
  <div class="label label--features">Lumera Spa &amp; Salon Software Features</div>

  <div class="feature" style="left:32px;top:75px"><h3>APPOINTMENT SCHEDULING</h3><p>Easily manage appointments and resources</p></div>
  <div class="feature" style="left:32px;top:116px"><h3>EMAIL MARKETING CAMPAIGNS</h3><p>Build your brand and keep clients engaged</p></div>
  <div class="feature" style="left:32px;top:157px"><h3>INVENTORY MANAGEMENT</h3><p>Track your inventory and sell more products</p></div>
  <div class="feature" style="left:32px;top:198px;width:160px"><h3>ONLINE BOOKING</h3><p>Provide your salon and spa clients with easy online booking</p></div>
  <div class="feature" style="left:32px;top:253px;width:160px"><h3>CLIENT MANAGEMENT</h3><p>Develop long-lasting relationships with your clients</p></div>

  <div class="feature" style="left:277px;top:75px"><h3>EMPLOYEE MANAGEMENT</h3><p>Save time and eliminate the stress</p></div>
  <div class="feature" style="left:277px;top:116px;width:200px"><h3>POINT OF SALE</h3><p>Complete transactions more efficiently and accurately</p></div>
  <div class="feature" style="left:277px;top:168px;width:180px"><h3>BUSINESS MANAGEMENT</h3><p>Salon owners can streamline business processes</p></div>

  <div class="barber-photo" role="img" aria-label="Barber in apron checking his phone in a barbershop"></div>

  <div class="why-band"></div>
  <div class="why-bottom" role="img" aria-label="Faded photo of stylists working in a salon"></div>
  <div class="label label--why">Why Lumera Spa &amp; Salon Software?</div>
  <p class="why-intro">For over 29 years, we have been helping salons, spas, barber shops, and other businesses to overcome their challenges and exceed their objectives. Our mission is to help you grow your business by developing an intuitive &amp; customizable software program and providing unparalleled customer service.</p>

  <div class="why-point" style="top:433px">
    <h3>DEDICATED TO YOU</h3>
    <p>Salons &amp; spas consistently rave about our customer support. We don't believe in "email support with 24-hour response times." When you call us, you talk to a live person who is committed to helping you in whatever way we can.</p>
  </div>
  <div class="why-point" style="top:499px">
    <h3>EASY TO USE</h3>
    <p>New technologies tend to be overwhelming. We've designed Lumera to be super simple to use. With our intuitive interface and familiar menus, you'll be a pro in no time.</p>
  </div>

  <div class="circle-photo" role="img" aria-label="Two women looking at a tablet together in a salon"></div>
</section>

</body>
</html>
```